Business Card Design, including supply of raw art files plus a vector diagram of the zelvon logo and

We need the business card design for a company that is launching a new exciting product. The brief requires the submission of the following once the final design is chosen:

- business card layout including raw files
- a composite vector image file of the zelvon logo and tag line
- a standalone vector image file of the zelvon logo

The product will be launched as a customer engagement app.

It has 4 core modules which enables a person to do multiple things - book tours and activities, order takeaways, search for local deals and offers. A universal currency is at the heart of this product. When you use the app, you earn cashback rewards when shopping or buying at any of the merchant partners across the modules as . These rewards can then be used as full or part payment when buying goods or services at these merchant partners.

The business card must help us build the brand, communicate the benefit of the brand's key focus - the ability to earn and burn this universal cashback ccurrency - across the 4 modules - booking of tours and activities, ordering, searching for local deals and payment.

We would like the design to use the brand's blue colour the hex colour is: 00
Dark grey : 646464
Darker blue shadow: 058bdd
Main Blue: 0084ff

We need to translate this into a CMYK print or spot colour print.

Both print options to be supplied as separate files.

An example of the base concept we have in mind is attached for your reference.

The font used by the brand is Proxima Nova.

Note: the duration has been set as 2 days.

Industry/Entity Type

Business

Contact Information for Business Card

Carla Mendoza
Marketing
W: www.zelvon.example
M: + 61 400555123
T: +61 2 5550 1473
A: Suite 7, Level 2, 14-18 Harwick Street, Sydney, NSW, 2000, Australia

Font styles to use
Sans Serif

Requirements
Must have
• zelVon logo and tagline
• address details
• zelVon icons as supplied
Nice to have
• would like to have the option of a spot varnish layer over the logo and icons at the back of the card

```html
<!DOCTYPE html>
<html lang="en">
<head>
<meta charset="utf-8">
<title>zelVon business card</title>
<link rel="stylesheet" href="https://fonts.googleapis.com/css2?family=PT+Sans:wght@400;700&family=Raleway:wght@200;300&display=swap">
<style>
  :root {
    --page-bg: #f2f5f5;
    --brand-sky: #55bcf9;
    --card-white: #ffffff;
    --ink-grey: #4a5558;
    --icon-grey: #4d5659;
  }
  html, body {
    margin: 0;
    padding: 0;
    width: 1200px;
    height: 1000px;
    overflow: hidden;
    background: var(--page-bg);
  }
  .canvas { display: block; width: 1200px; height: 1000px; }
  .card-shape { filter: drop-shadow(6px 8px 6px rgba(0,0,0,0.18)); }
  .card-back { fill: var(--brand-sky); }
  .card-front { fill: var(--card-white); }
  .brand-disc { fill: var(--card-white); }
  .brand-disc-blue { fill: var(--brand-sky); }
  .wordmark {
    font-family: "Raleway", sans-serif;
    font-weight: 200;
    fill: var(--card-white);
  }
  .wordmark-large { font-size: 146px; }
  .wordmark-in-disc { font-size: 46px; fill: var(--brand-sky); font-weight: 300; }
  .wordmark-front { font-size: 58px; font-weight: 300; fill: var(--card-white); }
  .tagline {
    font-family: "Raleway", sans-serif;
    font-weight: 300;
    font-size: 41px;
    fill: var(--card-white);
  }
  .module-icon { fill: var(--card-white); }
  .module-stroke { fill: none; stroke: var(--card-white); stroke-width: 4; stroke-linecap: round; }
  .module-label {
    font-family: "PT Sans", sans-serif;
    font-weight: 700;
    font-size: 12.5px;
    letter-spacing: 0.6px;
    fill: var(--card-white);
  }
  .person-name {
    font-family: "PT Sans", sans-serif;
    font-weight: 700;
    font-size: 34px;
    letter-spacing: 2px;
    fill: var(--ink-grey);
  }
  .person-role {
    font-family: "PT Sans", sans-serif;
    font-weight: 700;
    font-size: 25px;
    letter-spacing: 1px;
    fill: var(--brand-sky);
  }
  .contact-text {
    font-family: "PT Sans", sans-serif;
    font-size: 17px;
    letter-spacing: 1px;
    fill: var(--ink-grey);
  }
  .contact-icon { fill: var(--icon-grey); }
  .contact-icon-line { fill: none; stroke: var(--icon-grey); stroke-width: 2; }
  .contact-icon-cut { fill: var(--card-white); }
</style>
</head>
<body>
<svg class="canvas" viewBox="0 0 1200 1000" xmlns="http://www.w3.org/2000/svg">

  <!-- Back of card -->
  <g class="back-side">
    <path class="card-shape card-back" d="M417.5,37 H967 V476 H417.5 A219.5,219.5 0 0 1 417.5,37 Z"/>
    <circle class="brand-disc" cx="355" cy="228" r="100"/>
    <text class="wordmark wordmark-in-disc" x="355" y="244" text-anchor="middle">zelVon</text>
    <text class="wordmark wordmark-large" x="488" y="248" textLength="440" lengthAdjust="spacingAndGlyphs">zelVon</text>
    <text class="tagline" x="582" y="296" textLength="344" lengthAdjust="spacingAndGlyphs">the cloud currency</text>

    <!-- Cashback rewards -->
    <g class="module module-cashback">
      <circle class="module-icon" cx="528" cy="345" r="12"/>
      <text x="528" y="351" text-anchor="middle" font-family="PT Sans, sans-serif" font-weight="700" font-size="17" fill="#55bcf9">$</text>
      <path class="module-stroke" d="M512,334 a18,18 0 0 1 10,-12"/>
      <path class="module-icon" d="M520,316 l8,6 l-9,4 z"/>
      <path class="module-stroke" d="M544,356 a18,18 0 0 1 -10,12"/>
      <path class="module-icon" d="M536,374 l-8,-6 l9,-4 z"/>
    </g>
    <text class="module-label" x="530" y="397" text-anchor="middle">CashBack Rewards</text>

    <!-- Tours and activities -->
    <g class="module module-tours">
      <rect class="module-icon" x="637" y="330" width="50" height="36" rx="4"/>
      <rect class="module-icon" x="652" y="324" width="18" height="8" rx="2"/>
      <circle cx="662" cy="348" r="10" fill="#55bcf9"/>
      <circle class="module-icon" cx="662" cy="348" r="6"/>
    </g>
    <text class="module-label" x="661" y="397" text-anchor="middle">Tours &amp; Activities</text>

    <!-- Mobile ordering -->
    <g class="module module-ordering">
      <path class="module-stroke" d="M764,326 L796,368"/>
      <path class="module-stroke" d="M760,322 v10 M766,320 v10 M772,322 v10"/>
      <path class="module-stroke" d="M798,334 L770,368"/>
      <ellipse class="module-icon" cx="801" cy="327" rx="7" ry="10" transform="rotate(35 801 327)"/>
    </g>
    <text class="module-label" x="785" y="397" text-anchor="middle">Mobile Ordering</text>

    <!-- Local offers -->
    <g class="module module-offers">
      <path class="module-icon" d="M894,322 h22 v22 l-26,26 l-22,-22 z"/>
      <circle cx="908" cy="330" r="3.5" fill="#55bcf9"/>
    </g>
    <text class="module-label" x="892" y="397" text-anchor="middle">Local Offers</text>
  </g>

  <!-- Front of card -->
  <g class="front-side">
    <path class="card-shape card-front" d="M197,520 H748 A220,220 0 0 1 748,960 H197 Z"/>

    <text class="person-name" x="433" y="624" text-anchor="middle">CARLA MENDOZA</text>
    <text class="person-role" x="434" y="653" text-anchor="middle">Marketing</text>

    <!-- Web -->
    <circle class="contact-icon" cx="274" cy="703" r="13"/>
    <text x="274" y="706" text-anchor="middle" font-family="PT Sans, sans-serif" font-size="7" font-weight="700" fill="#ffffff">www</text>
    <text class="contact-text" x="312" y="708">www.zelvon.example</text>

    <!-- Mobile -->
    <circle class="contact-icon-line" cx="274" cy="755" r="12"/>
    <path class="contact-icon" d="M268,748 q-2,1 -1,5 q3,7 10,10 q3,1 4,-1 l1,-2 l-4,-3 l-2,2 q-4,-2 -6,-6 l2,-2 l-3,-4 z"/>
    <text class="contact-text" x="312" y="760">+61 400555123</text>

    <!-- Telephone -->
    <path class="contact-icon" d="M262,802 q12,-8 24,0 v4 h-6 v-3 h-12 v3 h-6 z"/>
    <rect class="contact-icon" x="265" y="806" width="18" height="12" rx="2"/>
    <circle class="contact-icon-cut" cx="274" cy="812" r="3"/>
    <text class="contact-text" x="312" y="812">+61 2 5550 1473</text>

    <!-- Address -->
    <path class="contact-icon" d="M274,872 l-7,-12 a8,8 0 1 1 14,0 z"/>
    <circle class="contact-icon-cut" cx="274" cy="856" r="3"/>
    <text class="contact-text" x="312" y="864">Suite 7, Level 2, 14-18 Harwick Street,</text>
    <text class="contact-text" x="312" y="891">Sydney, NSW, 2000, Australia</text>

    <circle class="brand-disc-blue" cx="785" cy="738" r="150"/>
    <text class="wordmark wordmark-front" x="785" y="758" text-anchor="middle">zelVon</text>
  </g>
</svg>
</body>
</html>
```